318 Diamond & Fastpitch Clinic 2017

Design a flyer that will promote our 2017 summer camp for boys and girls softball.

Weeks of
July 10th - 14th
July 17th - 21st.

Players ages 5 - 11.
Full day = 9:30am - 2:30pm half day = 9:30am - 11:30am.
$295 / full day : $195/ half day

Hosted by "318 Diamond" affiliated with the KV Meteors Touring Baseball & Softball Club and the Pine Hollow Junior League,

Camp Location PHJL, Lane 48C Maple Bluff.

PHone 555-284-7730, email info@318diamond.example

The color should be "Red white and blue color scheme" with dates and location standing out. 318 Logo should be prominent PHJL and Meteors smaller and secondary.

Feel free to use stock photo's if available. visit www.kvmeteors.example for more pictures and there are links for the 2017 summer camp there with possibly some more information.

Target Market(s)

to catch the eye of parents of players ages 5 - 11 already at little league or shopping in local stores

Colors
ec1f27
0355a3
ffffff

Requirements
Must have
• red white and blue design,
• 318 logo and summer camp prominent so it catches the eye and explains what it is right away.
• the meteors and pine hollow logo's a the bottom showing the affiliation.
Nice to have
• stock photo's or something showing players having a great time or a beautiful ballpark
Should not have
• to much clutter or hard to figure out what it's for

```html
<!DOCTYPE html>
<html lang="en">
<head>
<meta charset="utf-8">
<title>318 Diamond &amp; Fastpitch Clinic 2017</title>
<link href="https://fonts.googleapis.com/css2?family=Alfa+Slab+One&family=Oswald:wght@500;600;700&family=Montserrat:wght@500;600&display=swap" rel="stylesheet">
<style>
  :root{
    --red:#ec1f27;
    --blue:#0355a3;
    --navy:#1b1f4f;
    --ink:#0d0f1c;
    --white:#ffffff;
    --teal:#1fb3b8;
    --field:#4f7d23;
  }
  html,body{margin:0;padding:0;overflow:hidden;background:#ececec;}
  .flyer{position:relative;width:950px;height:1200px;overflow:hidden;
    font-family:"Oswald",sans-serif;color:var(--white);}
  .stadium{position:absolute;inset:0;
    background:
      radial-gradient(ellipse 55% 35% at 80% 22%, rgba(255,236,170,.85), rgba(255,236,170,0) 70%),
      radial-gradient(ellipse 60% 30% at 25% 18%, rgba(220,240,255,.8), rgba(220,240,255,0) 70%),
      linear-gradient(180deg,#2f6f9a 0%,#7fb3c9 22%,#cfe0c4 40%,#9fbf5a 55%,#5c8a25 70%,#2f4a17 100%);}
  .ball-hero{position:absolute;left:170px;top:150px;width:625px;height:600px;border-radius:50%;
    background:radial-gradient(circle at 45% 40%,#ffffff 0%,#eeebe6 55%,#cfcac2 100%);
    box-shadow:0 20px 40px rgba(0,0,0,.35);}
  .shapes{position:absolute;inset:0;}
  .brand{position:absolute;top:95px;left:0;width:950px;display:flex;justify-content:center;align-items:center;gap:16px;}
  .brand-dot{width:34px;height:34px;border-radius:50%;background:var(--blue);}
  .brand-name{font-family:"Alfa Slab One",serif;font-size:70px;line-height:1;color:var(--red);}
  .headline{position:absolute;left:0;width:950px;text-align:center;font-family:"Alfa Slab One",serif;
    color:var(--white);line-height:1;margin:0;
    text-shadow:
      0 0 0 var(--navy),5px 5px 0 var(--navy),-5px 5px 0 var(--navy),5px -5px 0 var(--navy),-5px -5px 0 var(--navy),
      8px 0 0 var(--navy),-8px 0 0 var(--navy),0 8px 0 var(--navy),0 -8px 0 var(--navy),10px 12px 0 var(--navy);}
  .headline-main{top:295px;font-size:118px;letter-spacing:1px;}
  .headline-sub{top:440px;font-size:66px;}
  .headline-year{top:530px;font-size:82px;}
  .tilt{position:absolute;left:0;width:950px;text-align:center;transform:rotate(-3.6deg);transform-origin:center;}
  .dates{top:800px;font-size:46px;font-weight:600;letter-spacing:.5px;}
  .dates .red{color:var(--red);}
  .ages{top:868px;font-family:"Alfa Slab One",serif;font-size:38px;letter-spacing:2px;}
  .hours{top:925px;font-size:31px;font-weight:500;}
  .hours .star{color:var(--red);}
  .prices{top:975px;display:flex;justify-content:center;align-items:center;gap:18px;padding-left:90px;box-sizing:border-box;}
  .price{font-size:92px;font-weight:700;color:var(--red);line-height:1;}
  .price-label{font-family:"Alfa Slab One",serif;font-size:34px;line-height:.95;text-align:left;}
  .price-star{font-size:40px;color:transparent;-webkit-text-stroke:2px var(--white);margin:0 10px;}
  .ball-small{position:absolute;left:58px;top:985px;width:112px;height:112px;border-radius:50%;
    background:radial-gradient(circle at 40% 35%,#ffffff,#d8d3cb);}
  .contact{position:absolute;left:22px;top:1098px;width:600px;height:78px;background:rgba(10,10,14,.92);
    font-family:"Montserrat",sans-serif;font-size:18px;font-weight:600;padding:8px 0 0 26px;box-sizing:border-box;}
  .contact-row{display:flex;align-items:center;gap:10px;height:30px;}
  .contact-row .gap{width:26px;}
  .location{color:var(--red);}
  .icon{width:18px;height:18px;flex:none;}
  .affiliates{position:absolute;left:660px;top:1083px;}
  .affiliates-label{font-family:"Montserrat",sans-serif;font-size:12px;font-weight:500;letter-spacing:.5px;}
  .badges{display:flex;gap:14px;margin-top:6px;align-items:center;}
  .badge-club{width:118px;height:56px;background:var(--navy);border:2px solid var(--white);}
  .badge-league{width:64px;height:64px;background:var(--white);}
</style>
</head>
<body>
<main class="flyer">
  <div class="stadium" role="img" aria-label="Brightly lit ballpark with stands and a green infield"></div>
  <div class="ball-hero" role="img" aria-label="Close-up of a large baseball with red stitching"></div>

  <svg class="shapes" width="950" height="1200" viewBox="0 0 950 1200" aria-hidden="true">
    <polygon points="170,560 475,765 780,560 740,560 475,728 210,560" fill="var(--navy)"/>
    <polygon points="222,560 475,720 728,560 700,560 475,700 250,560" fill="var(--white)"/>
    <polygon points="262,560 475,692 688,560" fill="#2a2f66"/>
    <polygon points="0,830 950,770 950,840 0,902" fill="var(--ink)"/>
    <polygon points="0,902 950,840 950,1075 0,1110" fill="var(--navy)" opacity=".95"/>
    <polygon points="0,1110 950,1075 950,1200 0,1200" fill="#1d2b12" opacity=".6"/>
  </svg>

  <div class="brand">
    <span class="brand-dot"></span>
    <span class="brand-name">318 DIAMOND</span>
  </div>

  <h1 class="headline headline-main">DIAMOND</h1>
  <p class="headline headline-sub">&amp; FASTPITCH CLINIC</p>
  <p class="headline headline-year">2017</p>

  <p class="tilt dates" style="margin:0">WEEKS OF <span class="red">JULY 10TH - 14TH ★ JULY 17TH - 21ST.</span></p>
  <p class="tilt ages" style="margin:0">PLAYERS AGES 5 - 11</p>
  <p class="tilt hours" style="margin:0">FULL DAY : 9:30AM - 2:30PM. <span class="star">★</span> HALF DAY : 9:30AM - 11:30AM.</p>
  <div class="tilt prices">
    <span class="price">$295</span><span class="price-label">FULL<br>DAY</span>
    <span class="price-star">★</span>
    <span class="price">$195</span><span class="price-label">HALF<br>DAY</span>
  </div>

  <div class="ball-small" role="img" aria-label="Small baseball"></div>

  <div class="contact">
    <div class="contact-row location">
      <svg class="icon" viewBox="0 0 20 20"><circle cx="10" cy="10" r="10" fill="var(--teal)"/><path d="M10 4a4 4 0 0 0-4 4c0 3 4 8 4 8s4-5 4-8a4 4 0 0 0-4-4z" fill="var(--white)"/><circle cx="10" cy="8" r="1.5" fill="var(--teal)"/></svg>
      CAMP LOCATION PHJL, LANE 48C MAPLE BLUFF.
    </div>
    <div class="contact-row">
      <svg class="icon" viewBox="0 0 20 20"><circle cx="10" cy="10" r="10" fill="var(--teal)"/><path d="M7 5l2 2-1 2c1 1.5 2 2.5 3 3l2-1 2 2-1.5 1.5C10 14 6 10 5.5 6.5z" fill="var(--white)"/></svg>
      555-284-7730
      <span class="gap"></span>
      <svg class="icon" viewBox="0 0 20 20"><circle cx="10" cy="10" r="10" fill="var(--teal)"/><rect x="5" y="6.5" width="10" height="7" fill="var(--white)"/><path d="M5 6.5l5 4 5-4" stroke="var(--teal)" fill="none"/></svg>
      info@318diamond.example
    </div>
  </div>

  <div class="affiliates">
    <div class="affiliates-label">AFFILIATED WITH</div>
    <div class="badges">
      <div class="badge-club" role="img" aria-label="KV Meteors Touring Baseball &amp; Softball Club badge"></div>
      <div class="badge-league" role="img" aria-label="Pine Hollow Junior League badge"></div>
    </div>
  </div>
</main>
</body>
</html>
```